Christmas 2024 ACE and ARENA

We need a greeting card (front and back) for Christmas and New Year 2025.
The design should be appropriate for the Christmas season and based on our current flyer (attached). Feel free to include graphics.
The contents of the flyer are attached as a PDF file.
The size/dimensions are attached as a PDF file!

Thank you!

Requirements
Must have
• Font Montserrat, modern design, not too much content

```html
<!DOCTYPE html>
<html lang="de">
<head>
<meta charset="utf-8">
<title>ACE and ARENA – Weihnachtskarte 2024</title>
<link rel="stylesheet" href="https://fonts.googleapis.com/css2?family=Montserrat:wght@400;700&family=Allura&display=swap">
<style>
  :root {
    --bg: #e8e6e6;
    --card: #000000;
    --gold: #fdc52f;
    --gold-dark: #6b5314;
    --white: #ffffff;
    --ink: #000000;
  }
  * { margin: 0; padding: 0; box-sizing: border-box; }
  html, body { width: 1200px; height: 1200px; overflow: hidden; }
  body {
    background: var(--bg);
    font-family: "Montserrat", Arial, sans-serif;
    position: relative;
  }
  .card {
    position: absolute;
    width: 277px;
    height: 494px;
    background: var(--card);
    overflow: hidden;
    box-shadow: 0 3px 10px rgba(0,0,0,0.35);
  }
  .card-front { left: 457px; top: 78px; }
  .card-back-1 { left: 151px; top: 623px; }
  .card-back-2 { left: 462px; top: 623px; }
  .card-back-3 { left: 773px; top: 623px; }

  .stripe { position: absolute; inset: 0; width: 277px; height: 494px; }

  .brand {
    position: absolute;
    top: 102px; left: 0; width: 100%;
    text-align: center;
    color: var(--gold);
    font-weight: 700;
    font-size: 25px;
    letter-spacing: 2px;
  }
  .tree-scene {
    position: absolute;
    left: 22px; top: 223px;
    width: 236px; height: 175px;
    background: radial-gradient(ellipse at 50% 60%, rgba(253,197,47,0.28), rgba(253,197,47,0.05) 70%);
  }
  .greeting-band {
    position: absolute;
    left: 0; bottom: 0;
    width: 100%; height: 95px;
    background: var(--gold);
    display: flex; align-items: center; justify-content: center;
    text-align: center;
    color: var(--ink);
    font-weight: 700;
    font-size: 15.5px;
    line-height: 22px;
  }

  .ornaments {
    position: absolute;
    top: 0;
    height: 97px;
    background: linear-gradient(180deg, rgba(253,197,47,0.05), rgba(253,197,47,0.25));
  }
  .ornaments-left { left: 3px; width: 54px; }
  .ornaments-right { left: 222px; width: 53px; }

  .salutation {
    position: absolute;
    left: 38px; top: 109px;
    width: 201px; height: 55px;
    background: var(--gold);
    color: var(--ink);
    font-weight: 700;
    font-size: 13.2px;
    line-height: 16.8px;
    text-align: center;
    display: flex; align-items: center; justify-content: center;
  }
  .message {
    position: absolute;
    left: 0; top: 197px; width: 100%;
    text-align: center;
    color: var(--white);
    font-size: 9.9px;
    line-height: 14.3px;
  }
  .message p + p { margin-top: 13.5px; }
  .closing {
    position: absolute;
    left: 0; top: 308px; width: 100%;
    text-align: center;
    color: var(--white);
    font-weight: 700;
    font-size: 9.9px;
  }
  .signatures {
    position: absolute;
    left: 0; top: 330px; width: 100%;
    list-style: none;
    text-align: center;
    color: var(--gold);
    font-family: "Allura", cursive;
    font-size: 15px;
  }
  .signatures li { height: 23.6px; line-height: 23.6px; }
  .signatures-wide li { height: 28.6px; line-height: 28.6px; }
  .team-sign {
    position: absolute;
    left: 0; top: 330px; width: 100%;
    text-align: center;
    color: var(--gold);
    font-size: 16px;
    line-height: 22px;
  }
</style>
</head>
<body>

<section class="card card-front">
  <svg class="stripe" viewBox="0 0 277 494" aria-hidden="true">
    <defs>
      <linearGradient id="front-fade" x1="0" y1="0" x2="0" y2="1">
        <stop offset="0" stop-color="#6b5314" stop-opacity="0.75"/>
        <stop offset="0.6" stop-color="#6b5314" stop-opacity="0"/>
      </linearGradient>
    </defs>
    <polygon points="114,0 191,0 0,285 0,170" fill="url(#front-fade)"/>
  </svg>
  <div class="brand">ACE ARENA</div>
  <div class="tree-scene" role="img" aria-label="Gold outline Christmas tree with a star, flanked by two reindeer silhouettes"></div>
  <div class="greeting-band">Frohe Weihnachten und<br>ein glückliches neues Jahr 2025!</div>
</section>

<section class="card card-back-1">
  <svg class="stripe" viewBox="0 0 277 494" aria-hidden="true">
    <defs>
      <linearGradient id="back-fade-1" x1="0" y1="1" x2="0" y2="0">
        <stop offset="0" stop-color="#6b5314" stop-opacity="0.75"/>
        <stop offset="0.7" stop-color="#6b5314" stop-opacity="0"/>
      </linearGradient>
    </defs>
    <polygon points="85,494 163,494 277,322 277,206" fill="url(#back-fade-1)"/>
  </svg>
  <div class="ornaments ornaments-left" role="img" aria-label="Hanging gold snowflakes and Christmas baubles"></div>
  <div class="ornaments ornaments-right" role="img" aria-label="Hanging gold snowflakes and Christmas baubles"></div>
  <div class="salutation">Liebe Kunden,<br>liebe Kooperationspartner &amp;<br>liebe Freunde,</div>
  <div class="message">
    <p>zum Jahresende ein herzliches<br>Dankeschön für die vertrauensvolle und<br>professionelle Zusammenarbeit.</p>
    <p>Das Team von ACE and ARENA wünscht ein<br>frohes Weihnachtsfest, erholsame Feiertage und<br>einen erfolgreichen Start in das neue Jahr 2025!</p>
  </div>
  <div class="closing">In diesem Sinne viele Grüße aus Tannfeld,</div>
  <ul class="signatures">
    <li>Bernd Kaltner</li>
    <li>Max Kaltner</li>
    <li>Verena Kaltner</li>
    <li>Karin Lössl</li>
    <li>Carla Wendt</li>
    <li>Sven Dobrinski</li>
  </ul>
</section>

<section class="card card-back-2">
  <svg class="stripe" viewBox="0 0 277 494" aria-hidden="true">
    <defs>
      <linearGradient id="back-fade-2" x1="0" y1="1" x2="0" y2="0">
        <stop offset="0" stop-color="#6b5314" stop-opacity="0.75"/>
        <stop offset="0.7" stop-color="#6b5314" stop-opacity="0"/>
      </linearGradient>
    </defs>
    <polygon points="85,494 163,494 277,322 277,206" fill="url(#back-fade-2)"/>
  </svg>
  <div class="ornaments ornaments-left" role="img" aria-label="Hanging gold snowflakes and Christmas baubles"></div>
  <div class="ornaments ornaments-right" role="img" aria-label="Hanging gold snowflakes and Christmas baubles"></div>
  <div class="salutation">Liebe Kunden,<br>liebe Kooperationspartner &amp;<br>liebe Freunde,</div>
  <div class="message">
    <p>zum Jahresende ein herzliches<br>Dankeschön für die vertrauensvolle und<br>professionelle Zusammenarbeit.</p>
    <p>Das Team von ACE and ARENA wünscht ein<br>frohes Weihnachtsfest, erholsame Feiertage und<br>einen erfolgreichen Start in das neue Jahr 2025!</p>
  </div>
  <div class="closing">In diesem Sinne viele Grüße aus Tannfeld,</div>
  <ul class="signatures signatures-wide">
    <li>Martin Greuling</li>
    <li>Werner Pohlak</li>
    <li>Sven Dobrinski</li>
  </ul>
</section>

<section class="card card-back-3">
  <svg class="stripe" viewBox="0 0 277 494" aria-hidden="true">
    <defs>
      <linearGradient id="back-fade-3" x1="0" y1="1" x2="0" y2="0">
        <stop offset="0" stop-color="#6b5314" stop-opacity="0.75"/>
        <stop offset="0.7" stop-color="#6b5314" stop-opacity="0"/>
      </linearGradient>
    </defs>
    <polygon points="85,494 163,494 277,322 277,206" fill="url(#back-fade-3)"/>
  </svg>
  <div class="ornaments ornaments-left" role="img" aria-label="Hanging gold snowflakes and Christmas baubles"></div>
  <div class="ornaments ornaments-right" role="img" aria-label="Hanging gold snowflakes and Christmas baubles"></div>
  <div class="salutation">Liebe Kunden,<br>liebe Kooperationspartner &amp;<br>liebe Freunde,</div>
  <div class="message">
    <p>zum Jahresende ein herzliches<br>Dankeschön für die vertrauensvolle und<br>professionelle Zusammenarbeit.</p>
    <p>Das Team von ACE and ARENA wünscht ein<br>frohes Weihnachtsfest, erholsame Feiertage und<br>einen erfolgreichen Start in das neue Jahr 2025!</p>
  </div>
  <div class="closing">In diesem Sinne viele Grüße aus Tannfeld,</div>
  <div class="team-sign">Team ACE and ARENA</div>
</section>

</body>
</html>
```